FENNOX TAB (Disposable Charger) Needs packaging with actual mock up!

We have a word document with all the information that we need on the package so feel free to be creative and design your own. It is a small condom wrapper for a one-time use phone charger.

Below I have attached the file with the dimensions of the package. And also some competitors packaging for examples only. Please don't copy them. We need to be different and cooler.

Our logo is also below called Fennox Tab(See charger for logo we want). The other ones are just examples.

```html
<!DOCTYPE html>
<html lang="en">
<head>
<meta charset="utf-8">
<title>Fennox Tab – Disposable Charger Wrapper</title>
<link rel="stylesheet" href="https://fonts.googleapis.com/css2?family=Montserrat:wght@400;500;700;800&display=swap">
<style>
  :root{
    --paper:#ffffff;
    --ink:#111111;
    --wrap-black:#000000;
    --shade-dark:#1a1a1a;
    --shade-mid:#2a2a2a;
    --green-light:#74b96a;
    --green-mid:#5f9f57;
    --green-deep:#4e8a48;
    --band-grey:#7a7a7a;
    --hanger:#d3d3d3;
    --caution-yellow:#f3e21a;
    --caution-red:#e2231a;
    --white:#ffffff;
  }
  html,body{margin:0;padding:0;overflow:hidden;background:var(--paper);}
  .canvas{width:918px;height:1200px;position:relative;overflow:hidden;background:var(--paper);}
  .dieline{position:absolute;left:0;top:0;}
  text{font-family:"Montserrat",sans-serif;}
  .dim-label{fill:var(--ink);font-size:16px;font-weight:400;}
  .dim-small{fill:var(--ink);font-size:6.5px;}
  .dim-line{stroke:var(--ink);stroke-width:1;fill:none;}
  .brand-word{fill:var(--green-light);font-weight:800;}
  .tagline{fill:var(--white);font-weight:700;font-size:11.5px;}
  .web{fill:var(--green-light);font-weight:700;}
  .band-text{fill:var(--white);font-weight:800;font-size:14.5px;}
  .charged{fill:var(--green-light);font-weight:800;font-size:15px;}
  .ready{fill:var(--white);font-weight:500;font-size:8.5px;letter-spacing:.6px;}
  .capacity{fill:var(--white);font-weight:700;font-size:10.5px;}
  .compat-head{fill:var(--white);font-weight:700;font-size:12px;}
  .feature-label{fill:#d8d8d8;font-size:6.3px;font-weight:400;}
  .icon{fill:var(--green-light);}
  .icon-line{stroke:var(--green-light);stroke-width:1.6;fill:none;}
  .dir-head{fill:var(--green-light);font-size:10px;font-weight:500;}
  .dir-line{fill:var(--white);font-size:10px;font-weight:500;}
  .dir-num{fill:var(--green-light);}
  .caution-text{fill:var(--white);font-size:9.6px;font-weight:500;}
  .caution-word{fill:var(--caution-red);}
  .spec{fill:var(--white);font-size:10px;font-weight:500;}
  .upc{fill:var(--ink);font-weight:800;font-size:17px;}
  .cert{fill:none;stroke:var(--green-light);stroke-width:1.4;}
</style>
</head>
<body>
<div class="canvas">
<svg class="dieline" width="918" height="1200" viewBox="0 0 918 1200" xmlns="http://www.w3.org/2000/svg">
  <defs>
    <linearGradient id="front-backdrop" x1="0" y1="1" x2="0.7" y2="0.25">
      <stop offset="0" stop-color="#5f9f57"/>
      <stop offset="0.35" stop-color="#2f5a2b"/>
      <stop offset="0.7" stop-color="#000000"/>
      <stop offset="1" stop-color="#1e1e1e"/>
    </linearGradient>
    <linearGradient id="back-backdrop" x1="0" y1="1" x2="1" y2="0">
      <stop offset="0" stop-color="#1e1e1e"/>
      <stop offset="0.45" stop-color="#000000"/>
      <stop offset="1" stop-color="#242424"/>
    </linearGradient>
  </defs>

  <g class="dimensions">
    <line class="dim-line" x1="96" y1="410" x2="843" y2="410"/>
    <path d="M96 410 l10 -5 v10z M843 410 l-10 -5 v10z" fill="#111"/>
    <text class="dim-label" x="470" y="404" text-anchor="middle">170mm</text>
    <line class="dim-line" x1="96" y1="428" x2="96" y2="448"/>
    <line class="dim-line" x1="118" y1="428" x2="118" y2="448"/>
    <line class="dim-line" x1="469" y1="428" x2="469" y2="448"/>
    <line class="dim-line" x1="821" y1="428" x2="821" y2="448"/>
    <line class="dim-line" x1="843" y1="428" x2="843" y2="448"/>
    <text class="dim-small" x="107" y="439" text-anchor="middle">5mm</text>
    <text class="dim-small" x="283" y="439" text-anchor="middle">80mm</text>
    <text class="dim-small" x="657" y="439" text-anchor="middle">80mm</text>
    <text class="dim-small" x="832" y="439" text-anchor="middle">5mm</text>

    <line class="dim-line" x1="59" y1="465" x2="59" y2="898"/>
    <path d="M59 465 l-5 10 h10z M59 898 l-5 -10 h10z" fill="#111"/>
    <text class="dim-label" transform="translate(50 683) rotate(-90)" text-anchor="middle">99mm</text>
    <line class="dim-line" x1="65" y1="465" x2="87" y2="465"/>
    <line class="dim-line" x1="65" y1="544" x2="87" y2="544"/>
    <line class="dim-line" x1="65" y1="898" x2="87" y2="898"/>
    <text class="dim-small" transform="translate(80 505) rotate(-90)" text-anchor="middle">18mm</text>
    <text class="dim-small" transform="translate(80 720) rotate(-90)" text-anchor="middle">81mm</text>
    <line class="dim-line" x1="853" y1="465" x2="875" y2="465"/>
    <line class="dim-line" x1="853" y1="544" x2="875" y2="544"/>
    <line class="dim-line" x1="853" y1="898" x2="875" y2="898"/>

    <line class="dim-line" x1="96" y1="912" x2="96" y2="932"/>
    <line class="dim-line" x1="118" y1="912" x2="118" y2="932"/>
    <line class="dim-line" x1="469" y1="912" x2="469" y2="932"/>
    <line class="dim-line" x1="821" y1="912" x2="821" y2="932"/>
    <line class="dim-line" x1="843" y1="912" x2="843" y2="932"/>
  </g>

  <g class="wrapper" transform="translate(87 456)">
    <rect width="766" height="454" fill="var(--wrap-black)" stroke="#333" stroke-width="1"/>

    <g class="front-panel">
      <rect class="front-backdrop" x="0" y="0" width="382" height="454" fill="url(#front-backdrop)" role="img" aria-label="Angular green and charcoal geometric background artwork"/>

      <path d="M146 44 a10 10 0 0 1 10 -10 h33 a12 12 0 0 1 24 0 h23 a10 10 0 0 1 10 10 v6 a10 10 0 0 1 -10 10 h-80 a10 10 0 0 1 -10 -10z" fill="var(--hanger)"/>

      <text class="brand-word" x="196" y="138" font-size="43" text-anchor="middle">FENNOX</text>
      <line x1="97" y1="155" x2="226" y2="155" stroke="var(--green-light)" stroke-width="2.4"/>
      <text class="brand-word" x="294" y="163" font-size="19" text-anchor="end">TAB</text>
      <text class="tagline" x="195" y="178" text-anchor="middle">Disposable Cell Phone Charger</text>

      <text class="web" x="267" y="252" font-size="18" text-anchor="middle">fennox-tab.com</text>
      <polygon points="148,261 382,261 382,308 192,308" fill="var(--band-grey)"/>
      <text class="band-text" x="193" y="281">Compatible with</text>
      <text class="band-text" x="193" y="302">Bio-degradable shell</text>

      <text class="charged" x="313" y="345" text-anchor="middle">Charged Up</text>
      <text class="ready" x="313" y="361" text-anchor="middle">READY FOR USE</text>

      <rect x="143" y="397" width="4" height="16" fill="var(--band-grey)"/>
      <rect x="149" y="397" width="68" height="17" rx="1" fill="var(--band-grey)"/>
      <text class="capacity" x="183" y="409.5" text-anchor="middle">2900mah</text>

      <circle cx="313" cy="395" r="13" fill="none" stroke="var(--green-deep)" stroke-width="5"/>
    </g>

    <g class="back-panel">
      <rect class="back-backdrop" x="382" y="0" width="384" height="454" fill="url(#back-backdrop)" role="img" aria-label="Dark charcoal geometric background artwork"/>

      <path d="M520 44 a10 10 0 0 1 10 -10 h35 a12 12 0 0 1 24 0 h21 a10 10 0 0 1 10 10 v6 a10 10 0 0 1 -10 10 h-80 a10 10 0 0 1 -10 -10z" fill="var(--hanger)"/>

      <text class="compat-head" x="576" y="81" text-anchor="middle">Compatible with</text>
      <text class="brand-word" x="576" y="109" font-size="25" text-anchor="middle">FENNOX</text>
      <line x1="516" y1="117" x2="594" y2="117" stroke="var(--green-light)" stroke-width="1.8"/>
      <text class="brand-word" x="636" y="124" font-size="11" text-anchor="end">TAB</text>

      <g class="features">
        <circle class="icon" cx="457" cy="146" r="4"/>
        <path class="icon-line" d="M457 137v-2 M457 155v2 M448 146h-2 M466 146h2 M451 140l-1.5-1.5 M463 152l1.5 1.5 M463 140l1.5-1.5 M451 152l-1.5 1.5"/>
        <text class="feature-label" x="457" y="164" text-anchor="middle">8hrs talk time</text>

        <path class="icon" d="M516 137 l-6 10 h4 l-2 8 l7 -11 h-4 z"/>
        <text class="feature-label" x="514" y="164" text-anchor="middle">Pre-Charged</text>

        <path class="icon" d="M570 154 q0 -14 15 -17 q-2 15 -15 17z"/>
        <text class="feature-label" x="577" y="164" text-anchor="middle">Biodegradable</text>
        <text class="feature-label" x="577" y="172" text-anchor="middle">Shell</text>

        <rect class="icon-line" x="624" y="141" width="15" height="10" rx="1"/>
        <rect class="icon" x="640" y="144" width="2" height="4"/>
        <text class="feature-label" x="632" y="164" text-anchor="middle">1800mAh</text>

        <path class="icon" d="M697 137 q6 8 6 12 a6 6 0 0 1 -12 0 q0 -4 6 -12z"/>
        <line x1="690" y1="140" x2="704" y2="154" stroke="var(--wrap-black)" stroke-width="1.6"/>
        <text class="feature-label" x="697" y="164" text-anchor="middle">Waterproof</text>

        <circle class="icon-line" cx="484" cy="180" r="7"/>
        <path class="icon-line" d="M484 176v4h3"/>
        <text class="feature-label" x="484" y="198" text-anchor="middle">3-year shelf life</text>

        <rect class="icon" x="533" y="175" width="18" height="10" rx="2"/>
        <path d="M544 176 l-4 4 h3 l-2 4" stroke="var(--wrap-black)" stroke-width="1.2" fill="none"/>
        <text class="feature-label" x="543" y="198" text-anchor="middle">Portable</text>

        <path class="icon" d="M597 175 h14 v5 a7 7 0 0 1 -14 0z"/>
        <path d="M600 179 l4 3 l4 -3" stroke="var(--wrap-black)" stroke-width="1.2" fill="none"/>
        <text class="feature-label" x="604" y="198" text-anchor="middle">Fits in pocket</text>

        <rect class="icon-line" x="654" y="173" width="7" height="14" rx="1"/>
        <rect class="icon-line" x="664" y="173" width="7" height="14" rx="1"/>
        <text class="feature-label" x="662" y="198" text-anchor="middle">Android</text>
        <text class="feature-label" x="662" y="205" text-anchor="middle">iOS + Type C</text>
      </g>

      <line x1="382" y1="212" x2="764" y2="212" stroke="var(--green-light)" stroke-width="1.6"/>

      <text class="dir-head" x="411" y="228">Directions</text>
      <text class="dir-line" x="411" y="242"><tspan class="dir-num">1.</tspan> Plug into your device and switch on pod.</text>
      <text class="dir-line" x="423" y="257">(For maximum charge, close all open apps)</text>
      <text class="dir-line" x="411" y="272"><tspan class="dir-num">2.</tspan> Pod will charge until light shuts off,</text>
      <text class="dir-line" x="423" y="287">or turn off for future use.</text>
      <text class="dir-line" x="411" y="302"><tspan class="dir-num">3.</tspan> Please recycle battery, the shell is biodegradable</text>
      <text class="dir-head" x="411" y="317">Total charge varies by device</text>

      <rect x="436" y="323" width="281" height="33" fill="none" stroke="var(--caution-yellow)" stroke-width="1.6"/>
      <text class="caution-text" x="576" y="337" text-anchor="middle"><tspan class="caution-word">Caution:</tspan> Don't get pod wet.</text>
      <text class="caution-text" x="576" y="350" text-anchor="middle">Do not disassemble device. Battery may get warm.</text>

      <text class="web" x="438" y="372" font-size="13">fennox-tab.com</text>
      <text class="spec" x="414" y="388">2900mAh Output 5V 1000ma</text>

      <g class="certifications">
        <rect class="cert" x="414" y="400" width="16" height="16" rx="2"/>
        <rect class="cert" x="441" y="400" width="16" height="16" rx="2"/>
        <polygon class="cert" points="477,400 489,416 465,416"/>
        <rect class="cert" x="496" y="400" width="16" height="16" rx="2"/>
        <circle class="cert" cx="531" cy="408" r="8"/>
        <circle class="cert" cx="557" cy="408" r="8"/>
      </g>

      <rect x="646" y="364" width="83" height="49" fill="var(--white)"/>
      <text class="upc" x="687.5" y="384" text-anchor="middle">UPC</text>
      <text class="upc" x="687.5" y="405" text-anchor="middle">Code</text>
    </g>
  </g>
</svg>
</div>
</body>
</html>
```